Design business card for Bright Harbour Coaching!

I am a personal development coach (like a life coach) and corporate trainer and need a professionally designed double sided business card.

It needs to contain the business logo (I'm happy for the designer to choose the layout of the logo as I am still working out the best option myself) and the following information:

Tamsin Varga
Personal Development Coach and Trainer

+61 (0)452 819 407 (written that way)
tamsin@bright-harbour.com

www.bright-harbour.com

```html
<!DOCTYPE html>
<html lang="en">
<head>
<meta charset="utf-8">
<title>Bright Harbour Coaching – Business Card</title>
<link rel="stylesheet" href="https://fonts.googleapis.com/css2?family=Cinzel:wght@400&family=Raleway:wght@500;600;700&display=swap">
<style>
  :root {
    --backdrop: #e9e7e4;
    --card-white: #ffffff;
    --ink: #555759;
    --teal: #0f8e99;
    --teal-deep: #0b6b74;
    --teal-light: #14a1ab;
    --white: #ffffff;
  }
  * { box-sizing: border-box; margin: 0; padding: 0; }
  html, body {
    width: 1200px; height: 1000px; overflow: hidden;
    background: var(--backdrop);
  }
  .canvas { position: relative; width: 1200px; height: 1000px; }

  .card {
    position: absolute; left: 265px; width: 665px; height: 397px;
    border-radius: 22px; overflow: hidden;
    box-shadow: 0 6px 14px rgba(0,0,0,0.25);
  }
  .card--front { top: 73px; background: var(--card-white); }
  .card--back  { top: 533px; background: var(--teal-deep); }

  .brand-name {
    position: absolute;
    font-family: "Cinzel", serif; font-weight: 400;
    line-height: 1; text-align: center;
  }
  .brand-name .line-main { display: block; font-size: 26px; letter-spacing: 0.5px; }
  .brand-name .line-sub  { display: block; font-size: 15px; letter-spacing: 3px; margin-top: 2px; }

  .card--front .brand-name { left: 38px; top: 122px; width: 265px; color: var(--ink); }
  .brand-dot {
    position: absolute; left: 148px; top: 58px;
    width: 48px; height: 48px; border-radius: 50%;
    background: var(--teal);
  }

  .contact { position: absolute; left: 40px; top: 206px; font-family: "Raleway", sans-serif; }
  .contact .person { font-size: 17px; font-weight: 700; color: var(--ink); }
  .contact .role { font-size: 15px; font-weight: 500; color: var(--teal); margin-top: 4px; }
  .contact .details { margin-top: 20px; list-style: none; }
  .contact .details li {
    display: flex; align-items: center; gap: 8px;
    font-size: 15px; font-weight: 500; color: var(--ink); height: 23px;
  }
  .contact .details svg { width: 14px; height: 14px; fill: var(--teal); flex: none; }

  .website {
    position: absolute; right: 40px; top: 261px;
    font-family: "Raleway", sans-serif; font-size: 15px; font-weight: 500; color: var(--ink);
  }
  .website strong { color: var(--teal); font-weight: 700; }

  .wave { position: absolute; left: 0; bottom: 0; width: 665px; height: 100px; }

  .card--back .brand-name { right: 38px; top: 293px; color: var(--white); }
</style>
</head>
<body>
<div class="canvas">

  <section class="card card--front" aria-label="Business card front">
    <span class="brand-dot" aria-hidden="true"></span>
    <div class="brand-name">
      <span class="line-main">BRIGHT HARBOUR</span>
      <span class="line-sub">COACHING</span>
    </div>

    <div class="contact">
      <p class="person">Tamsin Varga</p>
      <p class="role">Personal Development Coach and Trainer</p>
      <ul class="details">
        <li>
          <svg viewBox="0 0 24 24" aria-hidden="true"><path d="M6.6 10.8a15.1 15.1 0 0 0 6.6 6.6l2.2-2.2a1 1 0 0 1 1-.25 11.4 11.4 0 0 0 3.6.57 1 1 0 0 1 1 1V20a1 1 0 0 1-1 1A17 17 0 0 1 3 4a1 1 0 0 1 1-1h3.5a1 1 0 0 1 1 1c0 1.25.2 2.45.57 3.57a1 1 0 0 1-.25 1z"/></svg>
          +61 (0)452 819 407
        </li>
        <li>
          <svg viewBox="0 0 24 24" aria-hidden="true"><path d="M2 5h20v14H2z M3.5 6.5v.6l8.5 5.6 8.5-5.6v-.6z" fill-rule="evenodd"/></svg>
          tamsin@bright-harbour.com
        </li>
      </ul>
    </div>

    <p class="website">www.<strong>bright-harbour</strong>.com</p>

    <svg class="wave" viewBox="0 0 665 100" preserveAspectRatio="none" aria-hidden="true">
      <path d="M0 18 C140 62 360 72 665 0 L665 100 L0 100 Z" fill="var(--teal-light)"/>
      <path d="M0 36 C150 74 370 78 665 14 L665 100 L0 100 Z" fill="var(--white)"/>
      <path d="M0 42 C150 80 370 84 665 20 L665 100 L0 100 Z" fill="var(--teal-deep)"/>
    </svg>
  </section>

  <section class="card card--back" aria-label="Business card back">
    <div class="brand-name">
      <span class="line-main">BRIGHT HARBOUR</span>
      <span class="line-sub">COACHING</span>
    </div>
  </section>

</div>
</body>
</html>
```